Beauty Salon Business/Appointment Card Design

We need a business card and logo design for our beauty business called Velora Beauty.

The name Velora is taken from the Sumerian goddesss of love, procreation, war and being honest with oneself. Her name was written with a sign that represents a reed stalk tied into a loop at the top, often depicted with wings as well wearing lapis lazuli jewels.

We will be offering all spa and beauty services and want to create a peaceful, revitalising environment for people to come and be welcomed, enabling them to find the beauty within themselves.

We would also prefer simplicity and boldness in a design, as well as an element of individuality and reproducibility for letterheads and other marketing products.
Updates

Reason: Due to work commitments, closing the due date at this time of the morning (0026 hrs) is not practical. We wll review the designs during the day of Wednesday the 11th and make a decision by 1700 hrs Australian Central Standard Time. Thank you all for your input and time

Target Market(s)

as its a beauty salon business, target is predominantly female from 18-60 years of age

Industry/Entity Type

Environment

Contact Information for Business Card

Velora Beauty (this is the business name - and needs a designed logo name/icon to be incorporated)

Marnie - 0412 874 203

velorabeauty@quillnet.com.au

finding the beauty within (this is our business motto & can be in a different font from the rest)

Other font styles liked:
• always & forever; Beaked Tyrant

Requirements
Must have
• As these will also be doubling as appointment cards it is required that they be double sided in design with the reverse having the following information able to be written in:
day
date
time
Nice to have
• something that is different, catchy, instantly recognisable as this business

the front and back design should ideally be consistent and complimentary

```html
<!DOCTYPE html>
<html lang="en">
<head>
<meta charset="utf-8">
<title>Velora Beauty – Business &amp; Appointment Card</title>
<link rel="stylesheet" href="https://fonts.googleapis.com/css2?family=Shadows+Into+Light&display=swap">
<style>
  :root {
    --page-bg: #ecebe8;
    --cream: #f7f2d6;
    --label-cream: #f4edd3;
    --ink: #2a2230;
    --pink-deep: #b0469f;
    --pink-mid: #cd62bb;
    --pink-light: #e491d6;
    --pink-pale: #f4d9ee;
    --motto-pink: #c23ea9;
    --line-pink: #c86bb7;
  }
  * { box-sizing: border-box; margin: 0; padding: 0; }
  html, body {
    width: 1200px; height: 784px; overflow: hidden;
    background: var(--page-bg);
    font-family: "Shadows Into Light", cursive;
  }
  .canvas { position: relative; width: 1200px; height: 784px; }

  .card {
    position: absolute; width: 560px; height: 311px;
    overflow: hidden; border-radius: 3px;
    box-shadow: 0 2px 10px rgba(0,0,0,0.12);
  }

  /* ---------- Appointment side ---------- */
  .card--back {
    left: 40px; top: 60px;
    background: linear-gradient(180deg, var(--pink-light) 0%, var(--pink-mid) 55%, var(--pink-deep) 100%);
  }
  .card--back .flower-art {
    position: absolute; left: 330px; top: -30px; width: 220px; height: 200px;
    border-radius: 50%;
    background: radial-gradient(circle at 50% 50%, rgba(190,90,170,0.45) 0%, rgba(190,90,170,0.18) 55%, rgba(190,90,170,0) 72%);
  }
  .appointment-slip {
    position: absolute; left: 52px; top: 38px; width: 298px; height: 104px;
    background: var(--label-cream); border-radius: 6px;
    padding: 12px 22px 0 22px;
  }
  .appointment-row {
    display: flex; align-items: baseline; height: 27px;
    color: var(--pink-deep); font-size: 19px;
  }
  .appointment-row .field-label { width: 44px; }
  .appointment-row .write-line {
    flex: 1; border-bottom: 1.5px dotted var(--line-pink); transform: translateY(-4px);
  }
  .card--back .brand-name {
    position: absolute; right: 30px; top: 178px;
    font-size: 40px; color: var(--ink); line-height: 1;
  }

  /* ---------- Contact side ---------- */
  .card--front { left: 600px; top: 413px; background: var(--cream); }
  .card--front .flower-art {
    position: absolute; left: 330px; top: -20px; width: 260px; height: 270px;
    border-radius: 50%;
    background: radial-gradient(circle at 48% 50%, rgba(205,95,185,0.55) 0%, rgba(220,140,205,0.3) 50%, rgba(220,140,205,0) 72%);
  }
  .card--front .brand-name {
    position: absolute; left: 46px; top: 78px;
    font-size: 54px; color: var(--ink); line-height: 1;
  }
  .contact-band {
    position: absolute; left: 0; top: 178px; width: 412px; height: 70px;
    background: linear-gradient(90deg, var(--pink-light) 0%, var(--pink-mid) 100%);
    padding: 6px 0 0 34px;
  }
  .contact-band p {
    color: var(--pink-pale); font-size: 19px; line-height: 27px;
    letter-spacing: 0.5px;
  }
  .motto {
    position: absolute; left: 34px; top: 258px;
    color: var(--motto-pink); font-size: 21px; letter-spacing: 3px;
  }
</style>
</head>
<body>
<main class="canvas">

  <section class="card card--back" aria-label="Appointment side">
    <div class="flower-art" role="img" aria-label="Faint line-drawn flower illustration"></div>
    <div class="appointment-slip">
      <div class="appointment-row"><span class="field-label">day:</span><span class="write-line"></span></div>
      <div class="appointment-row"><span class="field-label">date:</span><span class="write-line"></span></div>
      <div class="appointment-row"><span class="field-label">time:</span><span class="write-line"></span></div>
    </div>
    <div class="brand-name">Velora Beauty</div>
  </section>

  <section class="card card--front" aria-label="Contact side">
    <div class="flower-art" role="img" aria-label="Pink line-drawn flower illustration"></div>
    <div class="brand-name">Velora Beauty</div>
    <div class="contact-band">
      <p>Marnie - 0412 874 203</p>
      <p>velorabeauty@quillnet.com.au</p>
    </div>
    <p class="motto">finding the beauty within . . .</p>
  </section>

</main>
</body>
</html>
```